Business Card - Rebranding for Consulting Firm

We are renaming and rebranding our consulting firm and need to raise the level of quality of our cards as part of that effort. We consult to leading high tech, life science and other innovation sector companies.

Need a two-sided business card design.

Side 1: (a) Company logo (b) tag line: Optimize Your Investment in Talent (c) Name (d) Title (e) Phone 1: Office (f) Phone 2: Mobile (g) email: person@HollowmereAdvisory.com

Side 2: Two lines of text: (a) Growth is Imperative. Change is Constant. Talent Executes Strategy. (b) We help you excel at all three.

Target Market(s)

Business and human resources executives and senior managers

Industry/Entity Type

Management Consulting

Contact Information for Business Card

Font styles to use
Sans Serif

Requirements
Must have
• clean, not too busy, but with a bit of creativity. Stick to the colors used in the attached logo
• appeal to high tech, life science companies
Nice to have
• prefer white background

```html
<!DOCTYPE html>
<html lang="en">
<head>
<meta charset="utf-8">
<title>Hollowmere Advisory – Business Card</title>
<link href="https://fonts.googleapis.com/css2?family=Montserrat:wght@400;500;600;700&display=swap" rel="stylesheet">
<style>
  :root{
    --page:#e9ecef;
    --brand-deep:#1d5f9c;
    --brand-mid:#1a87c0;
    --brand-light:#25a8e0;
    --card-blue:#1b6fab;
    --card-blue-faint:#3580b8;
    --ink-grey:#8a8f94;
    --white:#ffffff;
  }
  *{box-sizing:border-box;margin:0;padding:0}
  html,body{width:1200px;height:900px;overflow:hidden;background:var(--page);
    font-family:'Montserrat',sans-serif}
  .canvas{position:relative;width:1200px;height:900px}
  .card{position:absolute;left:300px;width:600px;height:343px;border-radius:22px;overflow:hidden;
    box-shadow:0 10px 30px rgba(0,0,0,.18)}
  .card--back{top:70px;background:var(--card-blue)}
  .card--front{top:487px;background:var(--white)}
  .card__band{position:absolute;left:0;right:0;bottom:0;height:10px;background:var(--brand-light)}

  /* back side */
  .back__mark{position:absolute;left:0;right:0;top:84px;text-align:center;font-size:46px;font-weight:600;
    color:var(--card-blue-faint);letter-spacing:-.5px;white-space:nowrap}
  .back__statement{position:absolute;left:46px;top:200px;color:var(--white);font-size:15.5px;font-weight:500;white-space:nowrap}
  .back__statement .dot{color:var(--brand-light);margin:0 4px}
  .back__promise{position:absolute;right:46px;top:226px;color:#4aa3dc;font-size:13px;letter-spacing:.5px;white-space:nowrap}
  .bar{position:absolute;bottom:10px;width:48px}
  .back__bar--white{left:42px;height:70px;background:var(--white)}
  .back__bar--mid{left:98px;height:48px;background:var(--brand-mid)}
  .back__bar--light{left:154px;height:30px;background:var(--brand-light)}

  /* front side */
  .front__brand{position:absolute;left:40px;top:124px;display:flex;align-items:center;gap:12px}
  .front__brand-square{width:22px;height:22px;background:var(--brand-mid)}
  .front__brand-name{font-size:30px;font-weight:600;color:var(--brand-deep);letter-spacing:-.5px;white-space:nowrap}
  .front__person{position:absolute;right:44px;top:38px;text-align:right}
  .front__name{font-size:20px;font-weight:700;color:var(--brand-deep);letter-spacing:.5px}
  .front__title{font-size:14px;color:var(--ink-grey);margin-top:2px}
  .front__rule{position:absolute;left:300px;right:44px;top:96px;height:2px;background:var(--brand-light)}
  .front__bar--light{left:412px;bottom:auto;top:158px;height:26px;width:40px;background:var(--brand-light)}
  .front__bar--mid{left:460px;bottom:auto;top:132px;height:52px;width:40px;background:var(--brand-mid)}
  .front__bar--deep{left:508px;bottom:auto;top:112px;height:72px;width:48px;background:var(--brand-deep)}
  .front__contact{position:absolute;left:40px;top:226px;border-top:2px solid var(--brand-light);padding-top:8px;width:420px}
  .contact__row{display:flex;align-items:center;gap:10px;font-size:15px;color:var(--brand-deep);line-height:22px}
  .contact__row svg{width:12px;height:12px;fill:none;stroke:var(--ink-grey);stroke-width:1.6}
  .front__tagline{margin-top:6px;font-size:14px;color:var(--ink-grey);letter-spacing:.4px}
</style>
</head>
<body>
<main class="canvas">

  <section class="card card--back" aria-label="Business card, back">
    <div class="back__mark">Hollowmere Advisory</div>
    <p class="back__statement">Growth is Imperative<span class="dot">•</span>Change is Constant<span class="dot">•</span>Talent Executes Strategy</p>
    <p class="back__promise">WE HELP YOU EXCEL AT ALL THREE.</p>
    <div class="bar back__bar--white"></div>
    <div class="bar back__bar--mid"></div>
    <div class="bar back__bar--light"></div>
    <div class="card__band"></div>
  </section>

  <section class="card card--front" aria-label="Business card, front">
    <div class="front__brand">
      <span class="front__brand-square"></span>
      <span class="front__brand-name">Hollowmere Advisory</span>
    </div>
    <div class="front__person">
      <p class="front__name">DANIEL MARSH</p>
      <p class="front__title">Managing Director</p>
    </div>
    <div class="front__rule"></div>
    <div class="bar front__bar--light"></div>
    <div class="bar front__bar--mid"></div>
    <div class="bar front__bar--deep"></div>

    <div class="front__contact">
      <p class="contact__row">
        <svg viewBox="0 0 12 12" aria-hidden="true"><rect x="3" y="1" width="6" height="10" rx="1"/><line x1="5" y1="9" x2="7" y2="9"/></svg>
        +00 7300 118 452
      </p>
      <p class="contact__row">
        <svg viewBox="0 0 12 12" aria-hidden="true"><path d="M2 2c0 5 3 8 8 8l1-2-2-1-1 1c-2-1-3-2-4-4l1-1-1-2z"/></svg>
        +00 2040 611 927
      </p>
      <p class="contact__row">
        <svg viewBox="0 0 12 12" aria-hidden="true"><rect x="1" y="3" width="10" height="7"/><path d="M1 3l5 4 5-4"/></svg>
        person@HollowmereAdvisory.com
      </p>
      <p class="front__tagline">OPTIMIZE YOUR INVESTMENT IN TALENT</p>
    </div>
    <div class="card__band"></div>
  </section>

</main>
</body>
</html>
```